Business card design needed

A earthmoving company, in the background would be good if there could be a picture of a (scraper), we have a business card already with petal press you may be able to see that?

Industry/Entity Type

Business

Contact Information for Business Card

Company name: Brackenridge Earthmoving

Lionel Brackenridge
314 Wirrabilla-Thornvale Rd
Mount Pellow
4918
0437 962 615
lionel_brackenridge@mailfern.example

on the rear of the card
Equipment Hire and Contract

All Earthmoving, Mining and Civil Contruction

```html
<!DOCTYPE html>
<html lang="en">
<head>
<meta charset="utf-8">
<title>Brackenridge Earthmoving – Business Card</title>
<link rel="stylesheet" href="https://fonts.googleapis.com/css2?family=Arimo:wght@400;700&display=swap">
<style>
  :root {
    --amber: #f0ab00;
    --band-black: #070707;
    --ink: #0a0a0a;
    --steel: #c9cdcd;
    --sky-deep: #3d6fae;
    --sky-light: #dbe6ee;
    --dust: #a8763a;
    --dust-dark: #4a3018;
  }
  * { margin: 0; padding: 0; box-sizing: border-box; }
  html, body {
    width: 1200px;
    height: 693px;
    overflow: hidden;
    background: #ffffff;
  }
  .card {
    position: relative;
    width: 1200px;
    height: 693px;
    background: var(--amber);
    font-family: "Arimo", Arial, sans-serif;
    overflow: hidden;
  }
  .photo-sky {
    position: absolute;
    left: 0; top: 0;
    width: 466px; height: 102px;
    background: linear-gradient(160deg, var(--sky-deep) 0%, #7fa2c8 45%, var(--sky-light) 100%);
  }
  .photo-scraper {
    position: absolute;
    left: 0; top: 305px;
    width: 466px; height: 388px;
    background: linear-gradient(180deg, #6f9fc4 0%, #c9d9e0 38%, #b89a62 55%, var(--dust) 75%, var(--dust-dark) 100%);
  }
  .brand-band {
    position: absolute;
    left: 0; top: 102px;
    width: 1200px; height: 203px;
    background: var(--band-black);
  }
  .brand-square {
    position: absolute;
    left: 118px; top: 31px;
    width: 224px; height: 140px;
    background: var(--steel);
  }
  .brand-name {
    position: absolute;
    left: 565px; top: 34px;
    color: var(--amber);
    font-weight: 700;
    font-size: 55px;
    line-height: 68px;
    letter-spacing: 1px;
    text-transform: uppercase;
  }
  .band-pointer {
    position: absolute;
    left: 500px; top: 304px;
    width: 36px; height: 34px;
  }
  .contact {
    position: absolute;
    left: 507px; top: 362px;
    color: var(--ink);
    font-size: 33px;
    line-height: 45px;
    font-style: normal;
  }
  .contact-email {
    position: absolute;
    left: 497px; top: 590px;
    color: var(--ink);
    font-size: 33px;
    line-height: 45px;
  }
</style>
</head>
<body>
  <main class="card">
    <div class="photo-sky" role="img" aria-label="Blue sky with white clouds"></div>
    <div class="photo-scraper" role="img" aria-label="Yellow earthmoving scraper on a dusty dirt track under an evening sky"></div>

    <header class="brand-band">
      <div class="brand-square"></div>
      <h1 class="brand-name">Brackenridge<br>Earthmoving</h1>
    </header>

    <svg class="band-pointer" viewBox="0 0 36 34" aria-hidden="true">
      <polygon points="0,0 36,0 18,34" fill="#070707"/>
    </svg>

    <address class="contact">
      Lionel Brackenridge<br>
      314 Wirrabilla-Thornvale Rd<br>
      Mount Pellow<br>
      4918 0437 962 615
    </address>

    <p class="contact-email">lionel_brackenridge@mailfern.example</p>
  </main>
</body>
</html>
```